International Clinical Software Company needs a new business card design

We are looking for a new business card design for our company that has recently expanded into the UK market, making us a multinational company.
After having rebranded our website and produced a new style guide, we are looking for a business card that is creative and attention grabbing, while being consistent with the style and colour scheme used on the new website, www.pennick.care
We produce care management technology for the aged care market, but the main aspect we aim to communicate is the human element of our software, and the way it assists in providing better care for aged people, and stronger relationships between aged people and the staff that care for them.
Our current business card is a dark green with gold text, which makes the text quite difficult to read, not very aesthetically appealing and the colour scheme looks quite dated.
We would like something fresh and modern, that can still be colourful but doesn't use large blocks of dark colour, and uses the colours within our logo.
Something tying in with the leaves that are used in our logo could work quite nicely, along with the Autumn/Fall colours of soft greens, yellows and reds (also in our existing logo). However also happy to look at fresh, completely out of the box ideas we may not have yet considered.
Target Market(s)
The people that receive this business card work in the aged card or health industry and are either corporate/management level staff or clinical (Registered Nurses, care workers etc.)
Industry/Entity Type
Health Product
Contact Information for Business Card
Company Name - PennickCare
Company locations: United Kingdom, Australia, New Zealand
Staff Details:
Staff name: Dermot Marlow
Staff job title: Executive Chairman
Staff email: d.marlow@pennick.care
Office phone number: 01632 960481
Other font styles liked:
- Calibri
Requirements
Must have
- Must include the PennickCare brand name in it's current font
- Must include logo (3 leaves in gold circle)
- Must include Business Card Details
Nice to have
- Elements of gold
- White space
- Something autumn themed but not too cliched
Should not have
- No blue - used by a major competitor and we would like to differentiate from them
- Large blocks of dark green colour (the green that appears in our leaves on the logo on our current business card is the background colour and it is far too dark)

```html
<!DOCTYPE html>
<html lang="en">
<head>
<meta charset="utf-8">
<title>PennickCare – Business Card</title>
<link href="https://fonts.googleapis.com/css2?family=Carlito:wght@400;700&display=swap" rel="stylesheet">
<style>
  :root {
    --mint: #3eebc4;
    --mint-soft: #b9f6e6;
    --white: #ffffff;
    --sage: #c9d3bd;
    --khaki: #d6cf8a;
    --rose: #c9787e;
    --tan: #c4a584;
    --gold: #f0c000;
    --ink: #1a1200;
    --mist: #f4f5f9;
  }
  * { margin: 0; padding: 0; box-sizing: border-box; }
  html, body {
    width: 1200px;
    height: 686px;
    overflow: hidden;
    background: var(--white);
  }
  .card {
    position: relative;
    width: 1200px;
    height: 686px;
    overflow: hidden;
    font-family: "Carlito", "Calibri", sans-serif;
    background: linear-gradient(90deg, var(--mint) 0%, var(--mint-soft) 22%, var(--white) 40%, var(--white) 100%);
  }
  .leaf-artwork {
    position: absolute;
    left: 340px;
    top: 0;
    width: 780px;
    height: 686px;
    background: linear-gradient(170deg, var(--white) 0%, var(--sage) 30%, var(--khaki) 58%, var(--rose) 92%);
    -webkit-mask-image: linear-gradient(90deg, transparent 0%, #000 30%, #000 80%, transparent 100%);
    mask-image: linear-gradient(90deg, transparent 0%, #000 30%, #000 80%, transparent 100%);
    opacity: 0.85;
  }
  .halo {
    position: absolute;
    right: -100px;
    top: 160px;
    width: 400px;
    height: 400px;
  }
  .brand-mark {
    position: absolute;
    left: 158px;
    top: 30px;
    width: 160px;
    height: 160px;
  }
  .brand-name {
    position: absolute;
    left: 18px;
    top: 205px;
    font-size: 104px;
    font-weight: 400;
    line-height: 1;
    color: var(--tan);
    letter-spacing: 1px;
  }
  .contact {
    position: absolute;
    left: 733px;
    top: 472px;
    list-style: none;
    font-size: 23px;
    font-weight: 700;
    line-height: 28px;
    color: var(--gold);
    text-shadow:
      -1px -1px 0 var(--ink), 1px -1px 0 var(--ink),
      -1px 1px 0 var(--ink), 1px 1px 0 var(--ink),
      0 0 2px var(--ink);
    white-space: nowrap;
  }
</style>
</head>
<body>
  <div class="card">
    <div class="leaf-artwork" role="img" aria-label="Large overlapping leaves in soft sage green, khaki yellow and rose red"></div>

    <svg class="halo" viewBox="0 0 400 400" aria-hidden="true">
      <circle cx="200" cy="200" r="190" fill="var(--mist)"/>
    </svg>

    <svg class="brand-mark" viewBox="0 0 160 160" aria-hidden="true">
      <circle cx="80" cy="80" r="76" fill="var(--white)" stroke="var(--tan)" stroke-width="5"/>
    </svg>
    <div class="brand-name">PennickCare</div>

    <ul class="contact">
      <li class="contact-name">Dermot Marlow</li>
      <li class="contact-title">Executive Chairman</li>
      <li class="contact-email">Email: d.marlow@pennick.care</li>
      <li class="contact-company">PennickCare</li>
      <li class="contact-locations">United Kingdom, Australia, New Zealand</li>
      <li class="contact-phone">Tel : 01632 960481</li>
    </ul>
  </div>
</body>
</html>
```